Design a New Business Card for Our Company

We are looking for fresh, unique, and a modern business card that reflects our roots as digital marketing agency focused on SEM.

Industry/Entity Type

Marketing

Contact Information for Business Card

looking for very unique out of the box designs. clean and modern that compliments our logo

Requirements
Must have
• colors should match our logo
• Front should have name, address, email, and phone/fax of the person, phone/fax are the same number
• back should have our url

```html
<!DOCTYPE html>
<html lang="en">
<head>
<meta charset="UTF-8">
<title>Corvane Solutions Business Card</title>
<link href="https://fonts.googleapis.com/css2?family=Lato:wght@400;700;900&display=swap" rel="stylesheet">
<style>
  :root {
    --bg: #b9bcbc;
    --card-white: #f4f4f2;
    --brand-blue: #4a8fcb;
    --brand-blue-light: #5a9ed6;
    --brand-blue-dark: #3f82c0;
    --ink-gray: #8e8e8e;
    --ink-dark: #4a4a4a;
    --white: #ffffff;
  }
  * { box-sizing: border-box; margin: 0; padding: 0; }
  html, body {
    width: 1200px;
    height: 900px;
    overflow: hidden;
  }
  body {
    background: var(--bg);
    font-family: "Lato", sans-serif;
    position: relative;
  }
  .card {
    position: absolute;
    width: 640px;
    height: 366px;
    border-radius: 3px;
    box-shadow: 0 8px 22px rgba(0,0,0,0.22);
  }

  /* Front card */
  .card-front {
    left: 280px;
    top: 64px;
    background: var(--card-white);
  }
  .front-brand {
    position: absolute;
    left: 40px;
    top: 0;
    width: 240px;
    height: 366px;
    display: flex;
    align-items: center;
    justify-content: center;
    gap: 12px;
  }
  .brand-dot {
    width: 30px;
    height: 30px;
    border-radius: 50%;
    background: var(--brand-blue);
    flex-shrink: 0;
  }
  .front-brand .brand-name {
    font-weight: 700;
    font-size: 34px;
    color: var(--brand-blue);
    letter-spacing: 0.5px;
  }
  .divider {
    position: absolute;
    left: 318px;
    top: 78px;
    width: 2px;
    height: 210px;
    background: var(--brand-blue);
  }
  .contact {
    position: absolute;
    left: 346px;
    top: 96px;
  }
  .person-name {
    font-size: 30px;
    line-height: 1.05;
  }
  .person-name .first { color: var(--ink-gray); font-weight: 400; }
  .person-name .last { color: var(--brand-blue); font-weight: 700; }
  .person-title {
    color: var(--brand-blue);
    font-size: 17px;
    margin-top: 2px;
    margin-bottom: 16px;
  }
  .contact-list { list-style: none; }
  .contact-list li {
    display: flex;
    align-items: center;
    gap: 10px;
    font-size: 17px;
    color: var(--ink-dark);
    line-height: 27px;
  }
  .contact-icon {
    width: 18px;
    height: 16px;
    flex-shrink: 0;
  }

  /* Back card */
  .card-back {
    left: 280px;
    top: 470px;
    background: linear-gradient(160deg, var(--brand-blue-light), var(--brand-blue-dark));
  }
  .back-brand {
    position: absolute;
    left: 0;
    right: 0;
    top: 138px;
    display: flex;
    align-items: center;
    justify-content: center;
    gap: 16px;
  }
  .back-brand .brand-dot { background: var(--white); width: 38px; height: 38px; }
  .back-brand .brand-name {
    font-weight: 700;
    font-size: 50px;
    color: var(--white);
  }
  .back-url {
    position: absolute;
    left: 0;
    right: 0;
    bottom: 40px;
    text-align: center;
    font-weight: 700;
    font-size: 19px;
    color: var(--white);
  }
</style>
</head>
<body>

  <section class="card card-front">
    <div class="front-brand">
      <span class="brand-dot"></span>
      <span class="brand-name">Corvane</span>
    </div>
    <div class="divider"></div>
    <div class="contact">
      <p class="person-name"><span class="first">Dara</span> <span class="last">Whitlow</span></p>
      <p class="person-title">Managing director</p>
      <ul class="contact-list">
        <li>
          <svg class="contact-icon" viewBox="0 0 18 16" aria-hidden="true">
            <path d="M2 5 Q9 0 16 5 L14 7 L11 5.5 L7 5.5 L4 7 Z" fill="var(--brand-blue)"/>
            <rect x="4" y="8" width="10" height="7" rx="1" fill="var(--brand-blue)"/>
          </svg>
          5550 1842 7731
        </li>
        <li>
          <svg class="contact-icon" viewBox="0 0 18 16" aria-hidden="true">
            <rect x="5" y="1" width="8" height="4" fill="var(--brand-blue)"/>
            <rect x="1" y="5" width="16" height="7" rx="1" fill="var(--brand-blue)"/>
            <rect x="5" y="10" width="8" height="5" fill="var(--brand-blue)" stroke="var(--card-white)" stroke-width="1"/>
          </svg>
          5550 1842 7731
        </li>
        <li>
          <svg class="contact-icon" viewBox="0 0 18 16" aria-hidden="true">
            <rect x="1" y="3" width="16" height="11" fill="var(--brand-blue)"/>
            <path d="M1 3 L9 10 L17 3" fill="none" stroke="var(--card-white)" stroke-width="1.4"/>
          </svg>
          dara@corvane-mail.com
        </li>
        <li>
          <svg class="contact-icon" viewBox="0 0 18 16" aria-hidden="true">
            <rect x="1.5" y="2" width="15" height="10" fill="none" stroke="var(--brand-blue)" stroke-width="1.6"/>
            <rect x="6" y="13" width="6" height="2" fill="var(--brand-blue)"/>
          </svg>
          www.corvane-web.com
        </li>
      </ul>
    </div>
  </section>

  <section class="card card-back">
    <div class="back-brand">
      <span class="brand-dot"></span>
      <span class="brand-name">Corvane Solutions</span>
    </div>
    <p class="back-url">www.corvane.com</p>
  </section>

</body>
</html>
```